Brightwater Court Services needs a business card

I need a business card design for a new company
For the last 10 years I have ran a tennis management company called Silver Hollow Racquet (www.silverhollowracquet.com)
The new company - Brightwater Court Services (BCS) will replace SHRA starting this winter
The goal of BCS will be to expand our operations into new clubs as well and a revenue stream from existing clubs with courtlinkhub.net
We plan to go regional in 2014 and then look outward from there

Target Market(s)

small to medium sized tennis facilities both public and private
Our market are the clubs - not the players
This includes private clubs, municipalities, recreation assc, etc

Industry/Entity Type

Business

Requirements
Must have
• Dale Huxley
• President
• 555-284-1937 Office
• 555-419-5062 Cell
• dhuxley@brightwatercourtservices.com
• www.brightwatercourtservices.com
Nice to have
• One of the unique benefits to a company joining BCS will be integration into our web based club software service - Courtlinkhub.net
• We have developed this turnkey service for small to medium sized clubs and re the exclusive providers of it
Should not have
• address or state

```html
<!DOCTYPE html>
<html lang="en">
<head>
<meta charset="utf-8">
<title>Brightwater Court Services – Business Card</title>
<link href="https://fonts.googleapis.com/css2?family=Saira:wght@400;500;700;800&display=swap" rel="stylesheet">
<style>
  :root {
    --backdrop: #bcbdbf;
    --card: #ffffff;
    --ink: #111111;
    --lime: #99cc00;
    --court-top: #1a2e22;
    --court-mid: #2d5238;
    --court-low: #3a6a45;
    --badge-grey: #d9d9d9;
    --badge-blue: #3b5998;
    --badge-sky: #4fb8e8;
    --badge-navy: #1d5a8c;
  }
  * { margin: 0; padding: 0; box-sizing: border-box; }
  html, body { width: 1200px; height: 1001px; overflow: hidden; }
  body {
    background: var(--backdrop);
    font-family: "Saira", sans-serif;
    color: var(--ink);
    position: relative;
  }
  .card {
    position: absolute;
    left: 223px;
    width: 754px;
    height: 430px;
    background: var(--card);
    box-shadow: 0 4px 12px rgba(0,0,0,0.45);
    overflow: hidden;
  }
  .card--front { top: 57px; }
  .card--back { top: 513px; }

  /* Front */
  .brand {
    position: absolute;
    left: 358px;
    top: 55px;
    display: flex;
    align-items: center;
    gap: 16px;
  }
  .brand__mark {
    width: 133px;
    height: 82px;
    background: var(--lime);
  }
  .brand__name {
    font-weight: 800;
    font-size: 26px;
    line-height: 26px;
    text-transform: uppercase;
    color: var(--ink);
  }
  .person { position: absolute; left: 54px; top: 178px; }
  .person__name { font-weight: 700; font-size: 28px; line-height: 34px; }
  .person__title { font-weight: 400; font-size: 20px; line-height: 26px; margin-top: 2px; }
  .contact { position: absolute; font-size: 18px; line-height: 27px; white-space: nowrap; }
  .contact--left { left: 54px; top: 281px; }
  .contact--left .mobile { font-size: 20px; }
  .contact--right { right: 44px; top: 255px; text-align: right; }
  .web-band {
    position: absolute;
    left: 0;
    bottom: 0;
    width: 754px;
    height: 66px;
    background: var(--lime);
    border-top-left-radius: 66px 66px;
    display: flex;
    align-items: center;
    justify-content: center;
  }
  .web-band__url {
    color: #ffffff;
    font-weight: 700;
    font-size: 27px;
    letter-spacing: 0.3px;
  }

  /* Back */
  .court-photo {
    position: absolute;
    inset: 0;
    background: linear-gradient(180deg, var(--court-top) 0%, var(--court-mid) 40%, var(--court-low) 100%);
  }
  .social-tab {
    position: absolute;
    right: 0;
    bottom: 0;
    width: 402px;
    height: 65px;
    background: var(--card);
    border-top-left-radius: 60px 65px;
  }
  .social-tab__badge {
    position: absolute;
    top: 7px;
    width: 52px;
    height: 52px;
    border-radius: 6px;
  }
  .badge--club { left: 63px; background: var(--badge-grey); }
  .badge--one { left: 154px; background: var(--badge-blue); }
  .badge--two { left: 243px; background: var(--badge-sky); }
  .badge--three { left: 328px; background: var(--badge-navy); }
</style>
</head>
<body>
  <section class="card card--front">
    <div class="brand">
      <div class="brand__mark"></div>
      <div class="brand__name">Brightwater<br>Court<br>Services</div>
    </div>
    <div class="person">
      <div class="person__name">DALE HUXLEY</div>
      <div class="person__title">PRESIDENT</div>
    </div>
    <div class="contact contact--left">
      <div class="mobile">M: 555-419-5062</div>
      <div>E: dhuxley@brightwatercourtservices.com</div>
    </div>
    <div class="contact contact--right">
      <div>P: 555-284-1937</div>
      <div>DDI: +00 0 000 00000</div>
      <div>F: +00 0 000 0000</div>
    </div>
    <div class="web-band">
      <span class="web-band__url">www.brightwatercourtservices.com</span>
    </div>
  </section>

  <section class="card card--back">
    <div class="court-photo" role="img" aria-label="Photo of a tennis ball resting on a white court line with the net blurred behind"></div>
    <div class="social-tab">
      <span class="social-tab__badge badge--club" role="img" aria-label="Club software badge"></span>
      <span class="social-tab__badge badge--one" role="img" aria-label="Social network badge"></span>
      <span class="social-tab__badge badge--two" role="img" aria-label="Social network badge"></span>
      <span class="social-tab__badge badge--three" role="img" aria-label="Social network badge"></span>
    </div>
  </section>
</body>
</html>
```